BrambleWare business card

Looking for business card design that supports our company/software values. We have 2 logo designs at the moment but open to change if you think you can enhance the brand. Check out website www.brambleware.com.au.

Target Market(s)

Education

Contact Information for Business Card

Name, title, mobile, email and website

Font styles to use
Sans Serif

Colors

Designer to choose colors to be used in the design.

Requirements
Must have
• BrambleWare logo with tree and tagline on rear side with dark grey background colour

```html
<!DOCTYPE html>
<html lang="en">
<head>
<meta charset="utf-8">
<title>BrambleWare business card</title>
<link rel="stylesheet" href="https://fonts.googleapis.com/css2?family=Montserrat:wght@400;500&display=swap">
<style>
  :root {
    --backdrop: #d0d1cc;
    --card-light: #ffffff;
    --card-dark: #1c1c1c;
    --accent: #f7b733;
    --ink: #3a3a3a;
    --ink-soft: #555555;
  }
  * { box-sizing: border-box; margin: 0; padding: 0; }
  html, body {
    width: 1200px; height: 1059px; overflow: hidden;
    background: var(--backdrop);
    font-family: "Montserrat", sans-serif;
  }
  .sheet {
    position: relative; width: 1200px; height: 1059px;
    display: flex; flex-direction: column; align-items: center; justify-content: center; gap: 56px;
  }
  .card {
    position: relative; width: 760px; height: 434px;
    border-bottom: 5px solid var(--accent);
    box-shadow: 0 14px 30px rgba(0,0,0,0.18);
  }
  .card--front { background: var(--card-light); }
  .card--back {
    background: var(--card-dark);
    display: flex; align-items: center; justify-content: center; gap: 22px;
  }

  .brand {
    position: absolute; left: 70px; top: 176px; width: 320px;
  }
  .brand__name {
    display: flex; align-items: center; gap: 12px;
    font-size: 36px; font-weight: 500; color: var(--ink); letter-spacing: 0.5px;
  }
  .brand__dot { width: 18px; height: 18px; border-radius: 50%; background: var(--accent); flex: none; }
  .brand__tagline {
    margin-top: 10px; margin-left: 30px;
    font-size: 13px; font-weight: 400; color: var(--ink-soft); letter-spacing: 0.4px;
  }

  .divider {
    position: absolute; left: 420px; top: 120px; width: 1.5px; height: 200px;
    background: var(--accent);
  }

  .contact {
    position: absolute; left: 455px; top: 108px; color: var(--ink);
  }
  .contact__name {
    font-size: 26px; font-weight: 500; color: var(--accent); letter-spacing: 1.5px; text-transform: uppercase;
  }
  .contact__title { font-size: 15px; margin-top: 2px; color: var(--ink-soft); }
  .contact__address { font-size: 15px; line-height: 1.45; margin-top: 14px; }
  .contact__list { list-style: none; margin-top: 12px; font-size: 15px; line-height: 1.6; }
  .contact__list li { display: flex; align-items: center; gap: 8px; }
  .contact__list svg { width: 12px; height: 12px; flex: none; }

  .back__name { font-size: 66px; font-weight: 500; color: #ffffff; letter-spacing: 0.5px; }
  .back__dot { width: 44px; height: 44px; border-radius: 50%; background: var(--accent); }
</style>
</head>
<body>
<main class="sheet">
  <section class="card card--front">
    <div class="brand">
      <div class="brand__name"><span class="brand__dot"></span>BrambleWare</div>
      <p class="brand__tagline">Learning Insights Suite</p>
    </div>
    <div class="divider"></div>
    <div class="contact">
      <h1 class="contact__name">Daniel Hartley</h1>
      <p class="contact__title">Director</p>
      <p class="contact__address">1820 Larkspur Lane<br>Fairview, MO 65812</p>
      <ul class="contact__list">
        <li>
          <svg viewBox="0 0 12 12" aria-hidden="true"><path d="M2.5 1.2l1.8 2.2-1 1.2c.7 1.5 1.8 2.6 3.2 3.2l1.2-1 2.1 1.8-1 1.7C5 10 1.8 6.9 1.2 2.4z" fill="var(--accent)"/></svg>
          555-014-2276
        </li>
        <li>
          <svg viewBox="0 0 12 12" aria-hidden="true"><rect x="1" y="2.5" width="10" height="7" fill="none" stroke="var(--accent)" stroke-width="1.2"/><path d="M1 3l5 3.6L11 3" fill="none" stroke="var(--accent)" stroke-width="1.2"/></svg>
          info@brambleware.com.au
        </li>
        <li>
          <svg viewBox="0 0 12 12" aria-hidden="true"><circle cx="6" cy="6" r="5" fill="none" stroke="var(--accent)" stroke-width="1.2"/><path d="M1 6h10M6 1c-2 2.5-2 7.5 0 10M6 1c2 2.5 2 7.5 0 10" fill="none" stroke="var(--accent)" stroke-width="1"/></svg>
          www.brambleware.com.au
        </li>
      </ul>
    </div>
  </section>

  <section class="card card--back">
    <span class="back__dot"></span>
    <span class="back__name">BrambleWare</span>
  </section>
</main>
</body>
</html>
```